Verdant Row

Currently www.verdantrow-example.com. This site was designed with a generic templet. However it is functional. I'm looking for a fun, fresh, and professional design. I also need help getting the XML for Searchly and Findo. I'm not a web designer and need help. I do not like my current sites narrow width.
Updates

All and all I'm liking the designs. The earlier ones seem better. Some seem that they are just taking my images and inputing them into a templet. I could have done that. The pictures are nice. Please keep in mind, functionality and updates. Please help us show our customers our how we are different. Safe Reliable Responsible are the key fundamentals, inside of these fundamentals show that were are customer service specialized. We are, Licensed, Insured, Drug Screened, Criminally Screened. Seems that people are putting up nice pictures but not capturing our values. Please help us market us on our website. Show our prospective customers why we are better, how we differentiate ourself from the competitors. Why choose us? Our flyers and cards are designed to drive our prospective customers to the website. If it looks identical with no pazaz like the card, then the marketing chain failed. I included our cards to help guide the thought process of our company. The link below is a feature I would love to have. This may be another project itself. I'm not sure if PH is the place to accomplish it. Below is a link for people to estimate there lawns with globe viewer. I would like to give a range of estimates using this technology. I have no clue how to accomplish it. If anyone knows how to who could do this, Please let me know. https://www.yardquote-example.com/showOrder/MOWLAWN/propertyDetails

Target Market(s)

We target residential customers 30-80 yr old. We also are expanding and placing a special emphasis on Business accounts. The main service is a mowing and landscape maintenance. Should be the main focus of the site.

Industry/Entity Type

Searchly

Coding

Coded - Design and coding required

Font styles to use
Sans Serif

Requirements
Must have
• I want this site to be fun and colorful. It still needs to be professional looking as not to deter business accounts. If you use photos, they must reflect Florida lawn. Note the architecture the homes, grass type, types of plants.
Should not have
• My current site is ok. I use it just as a

```html
<!DOCTYPE html>
<html lang="en">
<head>
<meta charset="utf-8">
<title>Verdant Row – Lawn Care</title>
<link rel="stylesheet" href="https://fonts.googleapis.com/css2?family=Lato:ital,wght@0,400;0,700;1,400;1,700;1,900&display=swap">
<style>
:root{
  --green:#5f9b2b;
  --green-dark:#4b8020;
  --red:#e53b24;
  --ink:#222;
  --muted:#333;
  --gray-band:#ececec;
  --footer:#444;
  --white:#fff;
}
*{box-sizing:border-box;margin:0;padding:0}
html,body{width:747px;height:1200px;overflow:hidden}
body{font-family:"Lato",sans-serif;color:var(--ink);background:var(--white);position:relative}
.abs{position:absolute}

/* header */
.site-header{position:absolute;left:0;top:0;width:747px;height:69px;
  background:linear-gradient(180deg,#2d78c8 0%,#5aa0dc 55%,#b9d8ef 100%)}
.brand{position:absolute;left:78px;top:20px;display:flex;align-items:center;gap:7px}
.brand-dot{width:22px;height:22px;border-radius:50%;background:var(--red)}
.brand-name{font-weight:900;font-size:22px;color:var(--green-dark);letter-spacing:-.2px}
.header-contact{position:absolute;right:83px;top:23px;text-align:right;font-size:10px;line-height:12px;color:#111}

/* nav */
.main-nav{position:absolute;left:0;top:69px;width:747px;height:21px;background:var(--green);display:flex;align-items:center}
.nav-item{position:absolute;top:0;height:21px;display:flex;align-items:center;gap:4px;color:var(--white);font-size:9.5px}
.nav-item svg{width:9px;height:9px;fill:var(--white)}
.nav-portal{background:#000;padding:0 6px;font-weight:700;font-style:italic}

/* hero */
.hero{position:absolute;left:0;top:90px;width:747px;height:343px;
  background:linear-gradient(180deg,#3f8fd6 0%,#9fcbee 30%,#e6f2fb 48%,#7dbb3c 56%,#4f9a22 78%,#3d8a18 100%)}
.hero-quote{position:absolute;left:0;top:36px;width:780px;text-align:center;color:var(--white);
  font-style:italic;font-size:23px;line-height:29.5px;text-shadow:0 1px 3px rgba(0,0,0,.55);letter-spacing:-.3px}
.hero-cta{position:absolute;left:72px;top:221px;width:260px;text-align:center;color:var(--white);
  font-style:italic;font-weight:700;font-size:15.5px;line-height:24px;text-shadow:0 1px 3px rgba(0,0,0,.6)}

/* section headings */
.section-title{position:absolute;left:0;width:747px;text-align:center;font-style:italic;font-weight:700;color:var(--green);font-size:18px}
.section-title .accent{color:var(--red)}
.title-rule{position:absolute;left:278px;width:178px;height:1px;background:var(--green)}
.title-rule::after{content:"";position:absolute;left:67px;top:-1px;width:44px;height:3px;background:var(--green)}

/* welcome */
.welcome-copy{position:absolute;left:80px;top:494px;width:374px;font-size:8.2px;line-height:12px;color:var(--muted);text-align:justify}
.welcome-copy p{margin-bottom:11.5px}
.photo{border:1px solid var(--red);border-radius:2px}
.welcome-photo{position:absolute;left:483px;top:498px;width:187px;height:135px;
  background:linear-gradient(180deg,#2f5a26 0%,#6a9a45 35%,#5fa630 70%,#4a8d22 100%)}

/* services */
.services-band{position:absolute;left:0;top:647px;width:747px;height:275px;background:var(--gray-band)}
.service-card{position:absolute;top:706px;width:136px}
.service-photo{width:136px;height:94px}
.service-name{margin-top:7px;text-align:center;font-style:italic;font-weight:700;font-size:10.5px;color:#111}
.service-text{margin-top:7px;height:49px;overflow:hidden;text-align:center;font-size:7.3px;line-height:12.2px;color:var(--muted)}
.read-more{display:block;margin:10px auto 0;width:60px;height:20px;line-height:20px;text-align:center;background:var(--green);
  color:var(--white);font-style:italic;font-weight:700;font-size:9px;border-radius:2px}

/* commercial */
.commercial-copy{position:absolute;left:80px;top:977px;width:587px;text-align:center;font-size:8.2px;line-height:12px;color:var(--muted)}
.commercial-copy p{margin-bottom:11.5px}
.cta-box{position:absolute;top:1074px;height:40px;background:var(--green);border-radius:2px;color:var(--white);
  font-style:italic;font-weight:700;font-size:9px;line-height:12px;text-align:center}
.cta-box svg{position:absolute;left:10px;top:8px}
.cta-box .cta-text{position:absolute;left:40px;right:14px;top:8px}
.cta-box .hl{color:var(--red)}

/* footer */
.site-footer{position:absolute;left:0;top:1132px;width:747px;height:68px;background:var(--footer)}
.copyright{position:absolute;left:0;top:12px;width:747px;text-align:center;color:var(--white);font-style:italic;font-weight:700;font-size:9.5px}
.pay-cards{position:absolute;left:322px;top:36px;display:flex;gap:2px}
.pay-card{width:24px;height:15px;border-radius:2px}
</style>
</head>
<body>

<header class="site-header">
  <div class="brand"><span class="brand-dot"></span><span class="brand-name">Verdant Row</span></div>
  <div class="header-contact">Toll Free: 800-555-YARD / 800-555-0196<br>Local: 321-555-0117</div>
</header>

<nav class="main-nav">
  <span class="nav-item" style="left:95px"><svg viewBox="0 0 10 10"><path d="M5 1 0 5h1.5v4h2.5V6.5h2V9h2.5V5H10z"/></svg>Home</span>
  <span class="nav-item" style="left:187px"><svg viewBox="0 0 10 10"><circle cx="5" cy="3" r="2.3"/><path d="M1 10c0-3 1.8-4.3 4-4.3S9 7 9 10z"/></svg>About Us</span>
  <span class="nav-item" style="left:290px"><svg viewBox="0 0 10 10"><rect x="0.5" y="3" width="9" height="6" rx="1"/><rect x="3.5" y="1.3" width="3" height="2" fill="none" stroke="#fff"/></svg>Services</span>
  <span class="nav-item" style="left:391px"><svg viewBox="0 0 10 10"><rect x="0.5" y="1.5" width="9" height="8" rx="1" fill="none" stroke="#fff"/><rect x="0.5" y="1.5" width="9" height="2"/></svg>Estimate</span>
  <span class="nav-item" style="left:494px"><svg viewBox="0 0 10 10"><rect x="0.5" y="2" width="9" height="6.5" rx="1"/><path d="M.8 2.4 5 5.6 9.2 2.4" fill="none" stroke="#5f9b2b"/></svg>Contact Us</span>
  <span class="nav-item nav-portal" style="left:595px;width:74px"><svg viewBox="0 0 10 10"><circle cx="5" cy="3" r="2.3"/><path d="M1 10c0-3 1.8-4.3 4-4.3S9 7 9 10z"/></svg>Client Portal</span>
</nav>

<section class="hero" role="img" aria-label="Rolling green lawn hills under a blue sky with a winding path, trees, and a cheerful red lawn mower">
  <p class="hero-quote" style="left:-16px">“We put our personal touch on Lawn Care”<br>Don't work for your lawn.<br>ENJOY YOUR LAWN.</p>
  <p class="hero-cta">Schedule a free estimate today.<br>It’s more affordable than you think.</p>
</section>

<h1 class="section-title" style="top:447px">Welcome To Verdant <span class="accent">Row</span></h1>
<div class="title-rule" style="top:475px"></div>
<div class="welcome-copy">
  <p>Verdant Row is SAFE, Reliable, and Responsible. We make sure that all of our lawn care professionals are licensed, insured, drug-free, background checks completed and legally eligible to work.</p>
  <p>Verdant Row offers convenient online bill pay, we accepts credit cards, and we pride ourselves with a great customer service department.</p>
  <p>If you are tired of lawn service companies that deliver poor quality, never call you back, have lousy communication skills, and are generally unprofessional and unreliable please consider giving Verdant Row a try.</p>
  <p>Try us with no risk and zero commitment. If you are not completely wowed by our unique service you may walk away without any pressure or hassle.</p>
</div>
<div class="welcome-photo photo" role="img" aria-label="Green lawn with sprinklers watering flower beds of purple and pink blooms"></div>

<section class="services-band"></section>
<h2 class="section-title" style="top:655px">Services</h2>
<div class="title-rule" style="top:684px"></div>

<article class="service-card" style="left:77px">
  <div class="service-photo photo" role="img" aria-label="Red lawn mower cutting thick green grass" style="background:linear-gradient(135deg,#b8322a 0%,#d44a3a 35%,#6e8d3a 55%,#557a2a 100%)"></div>
  <h3 class="service-name">Lawn Care</h3>
  <p class="service-text">We welcome the opportunity to provide full maintenance service. However, if all you need is a company to mow the yard, we are happy to help.</p>
  <span class="read-more">Read More</span>
</article>
<article class="service-card" style="left:229px">
  <div class="service-photo photo" role="img" aria-label="Flower bed with pink and red blooms in front of a house" style="background:linear-gradient(180deg,#d8d4c6 0%,#b06a7a 45%,#d94f8a 60%,#5e9a33 100%)"></div>
  <h3 class="service-name">Flower Bed Maintenance</h3>
  <p class="service-text">We are good at creating landscape designs that require minimal maintenance. However, your investment and beautiful landscape can quickly disappear if</p>
  <span class="read-more">Read More</span>
</article>
<article class="service-card" style="left:381px">
  <div class="service-photo photo" role="img" aria-label="Neatly trimmed hedge along a curved driveway" style="background:linear-gradient(180deg,#9fb88a 0%,#4f7d34 40%,#3f6e2a 75%,#8a8f88 100%)"></div>
  <h3 class="service-name">Trimming and Pruning</h3>
  <p class="service-text">Mowing the yard is only half the challenge. Bushes that are not consistently maintained hurt the appearance of even the best-kept property.</p>
  <span class="read-more">Read More</span>
</article>
<article class="service-card" style="left:533px">
  <div class="service-photo photo" role="img" aria-label="Brick garden path lined with colorful flowering plants and shrubs" style="background:linear-gradient(180deg,#5a8a3a 0%,#c95a7a 40%,#b88a6a 65%,#6a9a40 100%)"></div>
  <h3 class="service-name">Plant and Shrub Installation</h3>
  <p class="service-text">The addition of plants and shrubs is what ties a property all together. It has the ability to soften structures and provide curb appeal no matter what season it</p>
  <span class="read-more">Read More</span>
</article>

<h2 class="section-title" style="top:936px">Do you need property maintenance for a commercial property?</h2>
<div class="title-rule" style="top:967px"></div>
<div class="commercial-copy">
  <p>Verdant Row can establish a budget and remain within it. All costs are known. There are no hidden or indirect charges. Our safety practices, training procedures and comprehensive insurance, limit your exposure to liability as a result of careless or abusive use of equipment or chemicals.</p>
  <p>Verdant Row strives to be a one-stop 'Outdoor Service Provider'. If your outdoor services are not currently managed by one service provider let us show you the return on investment (ROI) earned by switching to Verdant Row. We solely focus on ground maintenance so you can focus on your business.</p>
  <p>Property managers love us because we make their job easy.</p>
</div>

<div class="cta-box" style="left:128px;width:237px">
  <svg width="24" height="24" viewBox="0 0 24 24"><rect width="24" height="24" rx="4" fill="#fff"/><path d="M7 5c1 0 2 2.5 2.3 3.5.2.8-1.2 1.4-1 2 .6 1.8 2.4 3.6 4.2 4.2.6.2 1.2-1.2 2-1 1 .3 3.5 1.3 3.5 2.3 0 1.3-1.5 3-3 3C10 19 5 14 5 8c0-1.5 1.7-3 2-3z" fill="#5f9b2b"/></svg>
  <span class="cta-text">For a refreshing lawn care experience<br>call <span class="hl">800-555-YARD</span> today</span>
</div>
<div class="cta-box" style="left:382px;width:237px">
  <svg width="30" height="26" viewBox="0 0 30 26"><path d="M29 1 1 12l8 3 3 10 4-7 7 5z" fill="#fff"/><path d="M9 15 27 3 12 17z" fill="#5f9b2b"/></svg>
  <span class="cta-text">You may also request a<br><span class="hl">Free Quote</span></span>
</div>

<footer class="site-footer">
  <p class="copyright">Copyright Verdant Row 2014. All Rights Reserved.</p>
  <div class="pay-cards" aria-label="Accepted payment cards">
    <span class="pay-card" style="background:#f2f2f2"></span>
    <span class="pay-card" style="background:#e6a23a"></span>
    <span class="pay-card" style="background:#4a8ad0"></span>
    <span class="pay-card" style="background:#e8e3da"></span>
  </div>
</footer>

</body>
</html>
```